Professional Business Cards

We need a nice looking, profession and modern business card for our new company. Our logo is attatched

Target Market(s)

Young Professionals

Industry/Entity Type

Financial

Contact Information for Business Card

FRONT

Vardane Ledger Pty Ltd
Level 22, Harbour Point, 48 Wattlebrook Ave
Sydney NSW 2000
ABN : 47 318 905 226

Owen Hadley - Chief Operations Officer
P : 02 9173 5528
M: 0418 356 091
owen@vardaneledger,com

BACK

- Cryptocurrency Exchange Services
- Cryptocurrency Mining Operations
- Cryptocurrency Investment Fund Offering

Font styles to use
Sans Serif

Colors
0255a3
9d9d9d

```html
<!DOCTYPE html>
<html lang="en">
<head>
<meta charset="utf-8">
<title>Vardane Ledger – Business Card</title>
<link rel="stylesheet" href="https://fonts.googleapis.com/css2?family=Exo+2:ital,wght@0,400;0,500;0,600;0,700;1,400&display=swap">
<style>
  :root {
    --brand-blue: #0255a3;
    --brand-blue-light: #1f6cc0;
    --brand-grey: #9d9d9d;
    --text-grey: #6f6f6f;
    --card-white: #ffffff;
    --stage-dark: #1b1b1b;
    --stage-mid: #303030;
  }
  * { box-sizing: border-box; margin: 0; padding: 0; }
  html, body {
    width: 1200px; height: 900px; overflow: hidden;
    font-family: "Exo 2", sans-serif;
  }
  body {
    background: radial-gradient(ellipse at 60% 30%, var(--stage-mid), var(--stage-dark) 75%);
    position: relative;
  }
  .card {
    position: absolute;
    left: 280px;
    width: 640px;
    height: 366px;
    box-shadow: 0 14px 30px rgba(0,0,0,.55);
    overflow: hidden;
  }

  /* Back side */
  .card-back {
    top: 60px;
    color: #fff;
  }
  .card-back .pattern {
    position: absolute; inset: 0;
    background: linear-gradient(135deg, var(--brand-blue) 0%, var(--brand-blue-light) 100%);
  }
  .card-back .wordmark {
    position: absolute;
    top: 120px; left: 0; right: 0;
    display: flex; justify-content: center; align-items: center; gap: 16px;
  }
  .mark-square {
    width: 34px; height: 34px; background: currentColor; flex: none;
  }
  .wordmark-name {
    font-weight: 700; font-size: 46px; letter-spacing: 1px; line-height: 1;
    text-transform: uppercase; white-space: nowrap;
  }
  .card-back .services {
    position: absolute; top: 232px; left: 0; right: 0;
    text-align: center; font-size: 15px; letter-spacing: .8px; line-height: 1.55;
  }

  /* Front side */
  .card-front {
    top: 474px;
    background: var(--card-white);
  }
  .name-band {
    position: absolute; top: 40px; left: 0;
    width: 480px; height: 66px;
  }
  .name-band svg { position: absolute; inset: 0; width: 100%; height: 100%; }
  .name-band .person {
    position: relative; padding: 8px 0 0 38px; color: #fff;
  }
  .person-name { font-size: 22px; font-weight: 500; letter-spacing: 1px; text-transform: uppercase; line-height: 1.1; }
  .person-role { font-size: 14px; font-style: italic; letter-spacing: .4px; }
  .card-front .wordmark {
    position: absolute; top: 116px; right: 34px;
    display: flex; align-items: center; gap: 10px;
    color: var(--brand-blue);
  }
  .card-front .wordmark .wordmark-name { font-size: 28px; }
  .card-front .mark-square { width: 22px; height: 22px; background: var(--brand-grey); }
  .contact-list {
    position: absolute; top: 178px; left: 38px;
    list-style: none; font-size: 16px; color: var(--text-grey); letter-spacing: 1px;
  }
  .contact-list li { display: flex; align-items: center; gap: 12px; line-height: 1.55; }
  .contact-list svg { width: 12px; height: 12px; fill: var(--brand-blue); flex: none; }
  .company {
    position: absolute; top: 270px; left: 38px;
  }
  .company-name {
    font-size: 16px; font-weight: 700; color: var(--brand-blue);
    letter-spacing: 1.3px; text-transform: uppercase; margin-bottom: 4px;
  }
  .company-address { font-size: 16px; color: var(--text-grey); letter-spacing: .8px; line-height: 1.4; }
  .abn {
    position: absolute; right: 40px; bottom: 26px;
    font-size: 16px; color: var(--text-grey); letter-spacing: 1px;
  }
</style>
</head>
<body>

<section class="card card-back" aria-label="Business card back">
  <div class="pattern" role="img" aria-label="Subtle blue diamond texture"></div>
  <div class="wordmark">
    <span class="mark-square"></span>
    <span class="wordmark-name">Vardane Ledger</span>
  </div>
  <p class="services">
    Cryptocurrency Mining Operations | Cryptocurrency Exchange Services<br>
    Cryptocurrency Investment Fund Offering
  </p>
</section>

<section class="card card-front" aria-label="Business card front">
  <div class="name-band">
    <svg viewBox="0 0 480 66" preserveAspectRatio="none" aria-hidden="true">
      <polygon points="0,0 440,0 480,66 0,66" fill="var(--brand-blue)"/>
    </svg>
    <div class="person">
      <p class="person-name">Owen Hadley</p>
      <p class="person-role">Chief Operations Officer</p>
    </div>
  </div>

  <div class="wordmark">
    <span class="mark-square"></span>
    <span class="wordmark-name">Vardane Ledger</span>
  </div>

  <ul class="contact-list">
    <li>
      <svg viewBox="0 0 24 24" aria-hidden="true"><path d="M6.6 10.8a15 15 0 0 0 6.6 6.6l2.2-2.2c.3-.3.7-.4 1-.2 1.1.4 2.3.6 3.6.6.6 0 1 .4 1 1V20c0 .6-.4 1-1 1A17 17 0 0 1 3 4c0-.6.4-1 1-1h3.5c.6 0 1 .4 1 1 0 1.3.2 2.5.6 3.6.1.3 0 .7-.2 1z"/></svg>
      02 9173 5528
    </li>
    <li>
      <svg viewBox="0 0 24 24" aria-hidden="true"><path d="M7 1h10a2 2 0 0 1 2 2v18a2 2 0 0 1-2 2H7a2 2 0 0 1-2-2V3a2 2 0 0 1 2-2zm0 3v14h10V4z"/></svg>
      0418 356 091
    </li>
    <li>
      <svg viewBox="0 0 24 24" aria-hidden="true"><path d="M2 5h20v14H2zm2 2v.5l8 5 8-5V7z"/></svg>
      owen@vardaneledger.com
    </li>
  </ul>

  <div class="company">
    <p class="company-name">Vardane Ledger Pty Ltd</p>
    <p class="company-address">Level 22, Harbour Point, 48<br>Wattlebrook Ave Sydney NSW 2000</p>
  </div>

  <p class="abn">ABN : 47 318 905 226</p>
</section>

</body>
</html>
```